Business Card - connecting 2 souls and beggining the journey of self discovery

Logo on the front
with tag line

On the back list of services and contact details

Seminars
workshops
Coaching
podcasts

Daniel Porthwick
Health & Wellbeing Life Coach
0491 372 815
daniel@wovenpathwellness.example
wovenpathwellness.example

Industry/Entity Type

Life Coaching

Contact Information for Business Card

I like the use of colour from the logo to be used. I'm not a fan of white.

Requirements
Must have
• My tagline: The journey home starts with you
Nice to have
• Use of colour that is in the mind body soul logo

```html
<!DOCTYPE html>
<html lang="en">
<head>
<meta charset="utf-8">
<title>Woven Path Wellness – Business Card</title>
<link href="https://fonts.googleapis.com/css2?family=Ubuntu:wght@400;500;700&display=swap" rel="stylesheet">
<style>
  :root {
    --ink: #566b74;
    --purple: #7a45f0;
    --pink: #f5477f;
    --yellow: #f0df38;
    --green: #5cf06a;
    --contact: #9577b4;
    --contact-soft: #8fbf8a;
    --card: #ffffff;
    --page: #ffffff;
  }
  * { margin: 0; padding: 0; box-sizing: border-box; }
  html, body { width: 1200px; height: 1200px; overflow: hidden; background: var(--page); }
  body { position: relative; font-family: "Ubuntu", sans-serif; }

  .card {
    position: absolute;
    left: 91px;
    width: 1018px;
    background: var(--card);
    overflow: hidden;
    outline: 1px solid #e6e8eb;
  }
  .card--front { top: 24px; height: 574px; }
  .card--back { top: 624px; height: 576px; }

  .splash { position: absolute; }
  .splash--purple { left: 0; top: 0; width: 270px; height: 210px;
    background: radial-gradient(ellipse at 10% 25%, var(--purple) 0 30%, rgba(122,69,240,.35) 50%, transparent 72%); }
  .splash--pink { right: 0; top: 0; width: 240px; height: 280px;
    background: radial-gradient(ellipse at 70% 35%, var(--pink) 0 28%, rgba(245,71,127,.35) 50%, transparent 72%); }
  .splash--yellow { left: 0; bottom: 0; width: 230px; height: 240px;
    background: radial-gradient(ellipse at 30% 80%, var(--yellow) 0 30%, rgba(240,223,56,.35) 52%, transparent 74%); }
  .splash--green { right: 0; bottom: 0; width: 210px; height: 180px;
    background: radial-gradient(ellipse at 80% 75%, var(--green) 0 30%, rgba(92,240,106,.35) 52%, transparent 74%); }

  .brand {
    position: absolute;
    left: 0; right: 0; top: 56px;
    display: flex; flex-direction: column; align-items: center;
  }
  .brand__mark {
    width: 140px; height: 140px; border-radius: 50%;
    background: var(--purple);
  }
  .brand__name {
    margin-top: 40px;
    font-weight: 400; font-size: 38px; letter-spacing: -0.5px;
    color: var(--ink);
  }
  .tagline {
    position: absolute; left: 0; right: 0; top: 292px;
    text-align: center;
    font-weight: 700; font-size: 50px; letter-spacing: 0.3px;
    color: var(--ink);
  }

  .services {
    position: absolute; left: 107px; top: 168px;
    list-style: none;
    font-weight: 700; font-size: 54px; line-height: 57px;
  }
  .services__item--seminars { color: var(--green); }
  .services__item--workshops { color: var(--yellow); }
  .services__item--coaching { color: var(--purple); }
  .services__item--podcasts { color: var(--pink); }

  .divider {
    position: absolute; left: 432px; top: 104px;
    width: 3px; height: 334px; background: var(--yellow);
  }

  .contact {
    position: absolute; left: 461px; top: 194px;
    font-style: normal;
    font-weight: 700; font-size: 29px; line-height: 38.5px;
    color: var(--contact);
    letter-spacing: 0.3px;
  }
  .contact__role-soft { color: var(--contact-soft); }
</style>
</head>
<body>
  <section class="card card--front">
    <div class="splash splash--purple" role="img" aria-label="Purple paint splatter"></div>
    <div class="splash splash--pink" role="img" aria-label="Pink paint splatter"></div>
    <div class="splash splash--yellow" role="img" aria-label="Yellow paint splatter"></div>
    <div class="splash splash--green" role="img" aria-label="Green paint splatter"></div>

    <div class="brand">
      <div class="brand__mark"></div>
      <div class="brand__name">Woven Path Wellness</div>
    </div>
    <p class="tagline">The journey home starts with you</p>
  </section>

  <section class="card card--back">
    <ul class="services">
      <li class="services__item services__item--seminars">Seminars</li>
      <li class="services__item services__item--workshops">Workshops</li>
      <li class="services__item services__item--coaching">Coaching</li>
      <li class="services__item services__item--podcasts">Podcasts</li>
    </ul>
    <div class="divider"></div>
    <address class="contact">
      <div class="contact__name">Daniel Porthwick</div>
      <div class="contact__role">Health &amp; Wellbeing <span class="contact__role-soft">Life Coach</span></div>
      <div class="contact__phone">0491 372 815</div>
      <div class="contact__email">daniel@wovenpathwellness.example</div>
      <div class="contact__web">wovenpathwellness.example</div>
    </address>
  </section>
</body>
</html>
```